Business Card Design Project

We need a business card design for a new company based in Singapore called 'Bright Ladder Pte Ltd'. We provide personal development training and emotional intelligence workshops. Our slogan is "Rise to your best self". We will not have a company address on the business card. Only phone number, email address and website address.

Target Market(s)

Adults age 25 to 45 years old.
Mostly working in a job.

Industry/Entity Type

Training

Colors
0255a2
f37123

```html
<!DOCTYPE html>
<html lang="en">
<head>
<meta charset="utf-8">
<title>Bright Ladder Pte Ltd – Business Cards</title>
<link href="https://fonts.googleapis.com/css2?family=Open+Sans:wght@400;600;700&display=swap" rel="stylesheet">
<style>
  :root {
    --navy: #1c3a6b;
    --navy-light: #4f86d8;
    --brand-blue: #0255a2;
    --orange: #f37123;
    --white: #ffffff;
    --backdrop: #e4e6ea;
  }
  * { margin: 0; padding: 0; box-sizing: border-box; }
  html, body {
    width: 1200px;
    height: 900px;
    overflow: hidden;
    background: var(--backdrop);
    font-family: "Open Sans", sans-serif;
  }
  .sheet {
    width: 1200px;
    height: 900px;
    display: flex;
    flex-direction: column;
    align-items: center;
    justify-content: center;
    gap: 32px;
  }
  .card {
    position: relative;
    width: 720px;
    height: 412px;
    background: var(--white);
    overflow: hidden;
    box-shadow: 0 6px 18px rgba(0, 0, 0, 0.18);
  }
  .card-shapes {
    position: absolute;
    inset: 0;
    width: 100%;
    height: 100%;
  }
  .brand {
    position: absolute;
    display: flex;
    align-items: center;
    gap: 12px;
  }
  .brand-dot {
    width: 40px;
    height: 40px;
    border-radius: 50%;
    background: var(--orange);
    flex-shrink: 0;
  }
  .brand-name {
    color: var(--brand-blue);
    font-weight: 700;
    font-size: 22px;
    letter-spacing: -0.2px;
    white-space: nowrap;
  }
  .tagline {
    position: absolute;
    color: var(--orange);
    font-weight: 400;
    white-space: nowrap;
  }
  .contact-list {
    position: absolute;
    right: 32px;
    top: 206px;
    list-style: none;
    text-align: right;
    color: var(--white);
    font-size: 15px;
    line-height: 27px;
    white-space: nowrap;
  }

  /* contact side */
  .card--contact .brand { left: 40px; top: 236px; }
  .card--contact .tagline { right: 46px; top: 58px; font-size: 22px; }

  /* brand side */
  .card--brand .brand { left: 62px; top: 178px; }
  .card--brand .brand-name { font-size: 26px; }
  .card--brand .brand-dot { width: 46px; height: 46px; }
  .card--brand .tagline { right: 40px; top: 42px; font-size: 15px; }
</style>
</head>
<body>
<main class="sheet">

  <section class="card card--contact" aria-label="Business card, contact side">
    <svg class="card-shapes" viewBox="0 0 720 412" aria-hidden="true">
      <defs>
        <linearGradient id="contactBand" x1="0" y1="0" x2="1" y2="0.3">
          <stop offset="0" stop-color="#1c3a6b"/>
          <stop offset="0.65" stop-color="#1f4278"/>
          <stop offset="1" stop-color="#3f5f95"/>
        </linearGradient>
      </defs>
      <path d="M240 0 L720 0 L720 412 L352 412 C372 260 335 110 240 0 Z" fill="url(#contactBand)"/>
      <path d="M262 0 C370 118 560 178 720 138 L720 0 Z" fill="#ffffff"/>
    </svg>

    <p class="tagline">"Rise to your best self"</p>

    <div class="brand">
      <span class="brand-dot"></span>
      <span class="brand-name">Bright Ladder Pte Ltd</span>
    </div>

    <ul class="contact-list">
      <li>t: 6555 0142 &nbsp;-&nbsp; f: 6555 0143</li>
      <li>e: info@brightladder.com</li>
      <li>w: brightladder.com</li>
    </ul>
  </section>

  <section class="card card--brand" aria-label="Business card, brand side">
    <svg class="card-shapes" viewBox="0 0 720 412" aria-hidden="true">
      <defs>
        <linearGradient id="brandSweep" x1="0" y1="0.4" x2="1" y2="0.6">
          <stop offset="0" stop-color="#1c3a6b"/>
          <stop offset="0.5" stop-color="#254c8a"/>
          <stop offset="1" stop-color="#4f86d8"/>
        </linearGradient>
      </defs>
      <path d="M120 0 L560 0 C460 78 240 80 120 0 Z" fill="#1c3a6b"/>
      <path d="M330 412 C410 250 560 118 720 92 L720 412 Z" fill="url(#brandSweep)"/>
    </svg>

    <p class="tagline">"Rise to your best self"</p>

    <div class="brand">
      <span class="brand-dot"></span>
      <span class="brand-name">Bright Ladder Pte Ltd</span>
    </div>
  </section>

</main>
</body>
</html>
```